Mirvanto general construction

We need an website that are similar to these websites:
https://www.dulcemor.com/en/
https://pomvilo.com/company/

but with a tweak. Do not copy the entire website but atleast similar and yet better than them.

For reference this our current website.
https://mirvanto.ph/

For the winning Designer please help us with the migration from our old website to the new redesign website.

```html
<!DOCTYPE html>
<html lang="en">
<head>
<meta charset="utf-8">
<title>Mirvanto General Construction</title>
<link rel="stylesheet" href="https://fonts.googleapis.com/css2?family=Anton&family=Oswald:wght@500;600;700&family=Plus+Jakarta+Sans:wght@400;500;600;700&family=Allura&display=swap">
<style>
:root{
  --orange:#ff4000;
  --cream:#e9e9de;
  --paper:#eeeee6;
  --ink:#161616;
  --dark:#1a1a1a;
  --grey:#a0a0a0;
  --tab-grey:#b4b4ae;
  --line:#d4d4cc;
}
*{margin:0;padding:0;box-sizing:border-box}
html,body{width:1200px;height:2175px;overflow:hidden}
body{position:relative;background:var(--dark);font-family:"Plus Jakarta Sans",sans-serif;color:var(--ink)}
.abs{position:absolute}
.display{font-family:"Oswald",sans-serif;text-transform:uppercase}

/* hero */
.hero{left:0;top:0;width:1200px;height:562px;background:var(--orange);overflow:hidden}
.hero-scene{left:0;top:330px;width:1200px;height:232px;background:linear-gradient(180deg,rgba(26,8,2,0) 0%,rgba(26,8,2,.55) 45%,#1c0a03 100%)}
.brand{left:182px;top:26px;display:flex;align-items:center;gap:8px;color:#fff;font-weight:700;font-size:17px;letter-spacing:.5px}
.brand-dot{width:14px;height:14px;border-radius:50%;background:#fff}
.nav{top:33px;display:flex;font-size:10px;font-weight:700;color:#fff}
.nav span{position:absolute;white-space:nowrap}
.phone{left:851px;top:27px;font-family:"Oswald",sans-serif;font-size:18px;font-weight:500;color:#fff}
.phone-icon{left:996px;top:27px;width:25px;height:25px;border-radius:50%;background:#111;display:flex;align-items:center;justify-content:center}
.headline{left:0;top:0}
.script{left:207px;top:178px;font-family:"Allura",cursive;font-size:52px;color:#1b1b1b;white-space:nowrap}
.tagline{right:178px;top:360px;text-align:right;color:#fff}
.tagline h2{font-family:"Oswald",sans-serif;font-weight:600;font-size:29px;line-height:31px;color:var(--cream);text-transform:uppercase}
.tagline p{font-size:10px;line-height:13px;margin-top:8px}

/* story */
.story{left:0;top:562px;width:1200px;height:716px;background:var(--paper)}
.signature{left:760px;top:685px;font-family:"Allura",cursive;font-size:40px;color:#222;white-space:nowrap}
.sig-role{left:933px;top:705px;font-size:8.5px;color:#555}
.year-hero{left:180px;top:809px;width:347px;height:175px;background:var(--orange)}
.photo{background:linear-gradient(160deg,#9a958a,#5d5a53)}
.caption{left:698px;top:994px;width:150px;font-size:8.5px;line-height:12.5px;color:#666}
.circle-btn{width:24px;height:24px;border-radius:50%;background:#fff;display:flex;align-items:center;justify-content:center;box-shadow:0 1px 3px rgba(0,0,0,.08)}
.to-top{width:20px;height:20px;background:var(--orange);border-radius:2px;display:flex;align-items:center;justify-content:center}
.tab{top:1128px;height:71px;border:2px solid var(--line);display:flex;align-items:center;justify-content:center;font-family:"Oswald",sans-serif;font-weight:700;font-size:64px;color:var(--tab-grey);letter-spacing:-1px}
.tab.is-active{background:#050505;border-color:#050505;color:#fff}

/* services */
.services-title{left:178px;top:1330px;font-family:"Oswald",sans-serif;font-weight:700;font-size:70px;color:#fff;letter-spacing:-1px}
.service-list{left:179px;top:1452px;width:518px}
.service-row{height:64px;border-top:1px solid #4a4a4a;display:flex;align-items:center;justify-content:space-between;padding:0 12px 0 10px;font-family:"Oswald",sans-serif;font-weight:600;font-size:29px;color:var(--grey);text-transform:uppercase}
.service-row.is-open{color:#fff}
.divider-v{left:697px;top:1452px;width:1px;height:228px;background:#4a4a4a}
.top-rule{left:179px;top:1452px;width:841px;height:1px;background:#4a4a4a}
.sub-list{left:718px;top:1471px;list-style:none;color:#fff;font-size:10px}
.sub-list li{height:27.5px;display:flex;align-items:center;gap:4px}
.sub-list li::before{content:"";width:0;height:0;border-left:4px solid var(--orange);border-top:3px solid transparent;border-bottom:3px solid transparent}
.service-photo{left:882px;top:1471px;width:138px;height:209px;background:linear-gradient(180deg,#1c86c9 0%,#3c97cc 40%,#d8661e 75%,#a7441a 100%)}
.read-more{left:718px;top:1668px;font-family:"Oswald",sans-serif;font-size:10px;color:#777;letter-spacing:.5px}
.read-dot{left:788px;top:1664px;width:22px;height:22px;border-radius:50%;background:var(--orange)}
.fade{left:0;top:1630px;width:1200px;height:52px;background:linear-gradient(180deg,rgba(26,26,26,0),var(--dark) 95%)}
.pill{left:520px;top:1715px;width:161px;height:36px;border:1px solid #fff;border-radius:18px;display:flex;align-items:center;justify-content:space-between;padding:0 4px 0 18px;font-family:"Oswald",sans-serif;font-weight:600;font-size:11.5px;color:#fff}
.pill-icon{width:26px;height:26px;border-radius:50%;background:#fff;display:flex;align-items:center;justify-content:center}

/* process */
.step{top:1829px;height:346px}
.step-num{position:absolute;top:22px;font-family:"Oswald",sans-serif;font-weight:600;font-size:66px;line-height:1}
.step-1{left:181px;width:146px;background:linear-gradient(180deg,#3a3d40,#1d1f21)}
.step-2{left:327px;width:147px;background:var(--paper)}
.step-3{left:474px;width:402px;background:var(--orange);color:#fff}
.step-4{left:876px;width:146px;background:#000;color:#fff}
.step-3 h3{position:absolute;left:26px;top:202px;font-family:"Oswald",sans-serif;font-weight:600;font-size:21px;text-transform:uppercase;letter-spacing:-.3px}
.step-3 p{position:absolute;left:26px;top:236px;width:260px;font-size:9.5px;line-height:13.5px}
.step-3 .cta{position:absolute;left:26px;top:296px;display:flex;align-items:center;gap:16px;font-family:"Oswald",sans-serif;font-weight:600;font-size:11.5px}
.cta-icon{width:24px;height:24px;border-radius:50%;background:#fff;display:flex;align-items:center;justify-content:center}
</style>
</head>
<body>

<section class="hero abs">
  <svg class="headline abs" width="1200" height="562" viewBox="0 0 1200 562" aria-hidden="true">
    <text x="184" y="312" textLength="829" lengthAdjust="spacingAndGlyphs" font-family="Anton, sans-serif" font-size="278" fill="#e9e9de">BUILDING</text>
  </svg>
  <div class="hero-scene abs" role="img" aria-label="Silhouettes of construction workers guiding a concrete bucket over scaffolding and rebar"></div>
  <div class="script abs">Constructions Service</div>

  <div class="brand abs"><span class="brand-dot"></span>Mirvanto</div>
  <nav class="nav abs">
    <span style="left:424px">HOME</span>
    <span style="left:491px">ABOUT US</span>
    <span style="left:564px">SERVICES</span>
    <span style="left:647px">PAGES</span>
    <span style="left:716px">CONTACT US</span>
  </nav>
  <div class="phone abs">+63 (0) 47 518-2093</div>
  <div class="phone-icon abs">
    <svg width="12" height="12" viewBox="0 0 24 24"><path d="M6.6 10.8a15 15 0 0 0 6.6 6.6l2.2-2.2c.3-.3.7-.4 1-.2 1.1.4 2.3.6 3.6.6.6 0 1 .4 1 1V20c0 .6-.4 1-1 1A17 17 0 0 1 3 4c0-.6.4-1 1-1h3.5c.6 0 1 .4 1 1 0 1.3.2 2.5.6 3.6.1.3 0 .7-.2 1z" fill="#fff"/></svg>
  </div>

  <svg class="abs" style="left:180px;top:376px" width="112" height="112" viewBox="0 0 112 112" aria-label="10 award winning construction company">
    <defs><path id="ring" d="M56 56 m-41 0 a41 41 0 1 1 82 0 a41 41 0 1 1 -82 0"/></defs>
    <circle cx="56" cy="56" r="55" fill="#c5300a" stroke="#ff6a3a" stroke-width="1"/>
    <text font-family="Plus Jakarta Sans, sans-serif" font-size="8.5" font-weight="600" fill="#fff" letter-spacing="1.6"><textPath href="#ring" startOffset="2%">10 AWARD WINNING - CONSTRUCTION COMPANY -</textPath></text>
    <circle cx="56" cy="56" r="13" fill="#fff"/>
  </svg>

  <div class="tagline abs">
    <h2>Beyond<br>Boundaries</h2>
    <p>Building spaces that inspire, connect,<br>and leave a lasting architectural legacy.</p>
  </div>
</section>

<section class="story abs"></section>
<svg class="abs" style="left:0;top:580px" width="1200" height="160" viewBox="0 580 1200 160" aria-label="From the start, we've delivered quality in both commercial and residential projects, building a reputation for excellence.">
  <g font-family="Oswald, sans-serif" font-weight="600" font-size="46">
    <text x="180" y="636" textLength="825" lengthAdjust="spacingAndGlyphs" fill="#161616">"FROM THE START, <tspan fill="#ff4000">WE'VE DELIVERED QUALITY</tspan> IN BOTH</text>
    <text x="180" y="681" textLength="817" lengthAdjust="spacingAndGlyphs" fill="#161616">COMMERCIAL AND RESIDENTIAL PROJECTS, BUILDING</text>
    <text x="180" y="727" textLength="506" lengthAdjust="spacingAndGlyphs" fill="#161616">A <tspan fill="#ff4000">REPUTATION FOR EXCELLENCE."</tspan></text>
  </g>
</svg>
<div class="signature abs">Lorena Vale</div>
<div class="sig-role abs">Founder, Stonevia</div>

<div class="year-hero abs">
  <svg width="347" height="175" viewBox="0 0 347 175" aria-label="1978">
    <text x="4" y="168" textLength="339" lengthAdjust="spacingAndGlyphs" font-family="Anton, sans-serif" font-size="226" fill="#efefe5">1978</text>
  </svg>
</div>
<div class="photo abs" style="left:538px;top:809px;width:150px;height:238px" role="img" aria-label="Archive photo of roofers working on a tiled roof"></div>
<div class="photo abs" style="left:698px;top:809px;width:150px;height:178px;background:linear-gradient(160deg,#b3ab9c,#6e685d)" role="img" aria-label="Archive photo of workers on timber scaffolding against a house"></div>
<div class="caption abs">This momentum propelled us toward larger, more ambitious construction milestones across regions and project types.</div>
<div class="photo abs" style="left:859px;top:809px;width:150px;height:210px;background:linear-gradient(160deg,#7d7b76,#3f3e3b)" role="img" aria-label="Archive photo of a crew on ladders against a building facade"></div>

<div class="circle-btn abs" style="left:966px;top:1088px"><svg width="12" height="10" viewBox="0 0 12 10"><path d="M11 5H1M5 1L1 5l4 4" fill="none" stroke="#222" stroke-width="1.3"/></svg></div>
<div class="circle-btn abs" style="left:996px;top:1088px"><svg width="12" height="10" viewBox="0 0 12 10"><path d="M1 5h10M7 1l4 4-4 4" fill="none" stroke="#222" stroke-width="1.3"/></svg></div>
<div class="to-top abs" style="left:1165px;top:1091px"><svg width="8" height="8" viewBox="0 0 8 8"><path d="M4 7V1M1.5 3.5 4 1l2.5 2.5" fill="none" stroke="#fff" stroke-width="1"/></svg></div>

<div class="tab abs" style="left:180px;width:159px">1978</div>
<div class="tab abs" style="left:350px;width:158px">1985</div>
<div class="tab abs is-active" style="left:518px;width:161px">1998</div>
<div class="tab abs" style="left:690px;width:159px">2008</div>
<div class="tab abs" style="left:860px;width:159px">2025</div>

<h2 class="services-title abs">SERVICES</h2>
<div class="top-rule abs"></div>
<div class="service-list abs">
  <div class="service-row is-open">Construction Solutions<svg width="24" height="16" viewBox="0 0 24 16"><path d="M0 8h22M15 1l7 7-7 7" fill="none" stroke="currentColor" stroke-width="2"/></svg></div>
  <div class="service-row">Civil Engineering Services<svg width="24" height="16" viewBox="0 0 24 16"><path d="M0 8h22M15 1l7 7-7 7" fill="none" stroke="currentColor" stroke-width="2"/></svg></div>
  <div class="service-row">Electrical Installations<svg width="24" height="16" viewBox="0 0 24 16"><path d="M0 8h22M15 1l7 7-7 7" fill="none" stroke="currentColor" stroke-width="2"/></svg></div>
  <div class="service-row">Craftsmanship &amp; Finishing<svg width="24" height="16" viewBox="0 0 24 16"><path d="M0 8h22M15 1l7 7-7 7" fill="none" stroke="currentColor" stroke-width="2"/></svg></div>
</div>
<div class="divider-v abs"></div>
<ul class="sub-list abs">
  <li>Residential Construction.</li>
  <li>Commercial Construction.</li>
  <li>Industrial Construction.</li>
  <li>Renovation &amp; Remodeling.</li>
  <li>Interior Fit-Out Works.</li>
</ul>
<div class="service-photo abs" role="img" aria-label="Tower crane beside a high-rise under construction against a blue sky"></div>
<div class="read-more abs">READ MORE</div>
<div class="read-dot abs"></div>
<div class="fade abs"></div>
<div class="to-top abs" style="left:1164px;top:1641px"><svg width="8" height="8" viewBox="0 0 8 8"><path d="M4 7V1M1.5 3.5 4 1l2.5 2.5" fill="none" stroke="#fff" stroke-width="1"/></svg></div>

<a class="pill abs">VIEW MORE SERVICES<span class="pill-icon"><svg width="10" height="10" viewBox="0 0 10 10"><path d="M2 8l6-6M3 2h5v5" fill="none" stroke="#111" stroke-width="1.2"/></svg></span></a>

<div class="step step-1 abs" role="img" aria-label="Dark glass skyscraper facade"><span class="step-num" style="left:28px;color:#fff">01</span></div>
<div class="step step-2 abs"><span class="step-num" style="left:28px;color:#111">02</span></div>
<div class="step step-3 abs">
  <span class="step-num" style="left:28px">03</span>
  <h3>Deliver &amp; Support With Excellence</h3>
  <p>After final inspections, we hand over your project on time and provide ongoing support to ensure long-lasting performance.</p>
  <div class="cta">GET IN TOUCH<span class="cta-icon"><svg width="10" height="10" viewBox="0 0 10 10"><path d="M2 8l6-6M3 2h5v5" fill="none" stroke="#111" stroke-width="1.2"/></svg></span></div>
</div>
<div class="step step-4 abs"><span class="step-num" style="left:27px">04</span></div>

</body>
</html>
```